company, product, services, opportunity presentation

Pelminor is a Payment Services Processor with value added product and services. We are focusing on the Payment Industry, Retail Merchants and Financial institutions. We have built total solution on AWS cloud to provide API based payment solutions such as Issuing of cards, Acquiring of payment transactions, Fraud prevention, Ecommerce, with customer facing APPs to provide dynamic virtual payment , 2FA and Passwordless sign in. Our focus is B2B .
We are developing our sales/investor pitch deck with slides covering company information, Market challengers (problems) that we are solving , Opportunities in the regional markets as well as global addressable Market for Payment cards. Pelminor Product and services offerings to meet these challenges and opportunities.
Total Addressable Market statistics and data. Specific to virtual payment cards, Second factor authentication and digital ID (passwordless). Primarily data and justification for reducing Ecommerce card abandonment and increasing Authorization rates
Pelminor Team and advisors’ slide. Current pipeline and customers. Use cases or case studies. Highlighting competitive advantage and USP. target clients and current pipline. Financials and projected spend in the next 2 years including target amount to raise fund. Solution and services slides and timeine of activities /roadmap
We need a PPT design to project better look and feel, crisp and eye catching graphic and design of the slides. clearer representation of key or salient points in all slides and information.

Target Market(s)

Financial Institutions, Retail (Merchants), Fintechs, Transportation

Industry/Entity Type

Cards and Payments Industry . Fraud prevention . Digital ID

Font styles to use
Sans Serif

Colors
F0912C
F2A743
F7CA91
FBE8D2
FDF5EE
EE7325
F08F49
F5BC92
FAE3D3
FDF4ED
A7469A
B969AE
D3A5CF
EDDBEB
F8F0F9
6B429C
8869AF
B7A5CE
E3DAEB
F3F0F8

Requirements
Must have
• problem to be solved, market challenges, market opportunities, product features and functionality. Use cases, Financial spend and funding. Team members and advisors. Timeline of roadmap for 2 years. competitive advantage and USP. Benefits to each customer segments
Nice to have
• Provision for future development on product and services. potentially covering other target markets such as Airlines, Insurance

```html
<!DOCTYPE html>
<html lang="en">
<head>
<meta charset="utf-8">
<title>Pelminor – Pitch Deck Overview</title>
<link href="https://fonts.googleapis.com/css2?family=Josefin+Sans:wght@300;400;700&family=Open+Sans:wght@400;600;700&display=swap" rel="stylesheet">
<style>
:root{
  --purple:#922F8E;
  --purple-deep:#5b1e58;
  --purple-soft:#EDDBEB;
  --orange:#F39A2F;
  --ink:#3a3a3a;
  --muted:#8c8c8c;
  --card:#f2f2f2;
  --white:#ffffff;
}
*{box-sizing:border-box;margin:0;padding:0}
html,body{width:1200px;height:1200px;overflow:hidden}
body{position:relative;background:var(--white);font-family:'Open Sans',sans-serif;color:var(--ink)}
.slide{position:absolute;width:480px;height:270px;background:var(--white);overflow:hidden;transform:scale(.6211);transform-origin:0 0;box-shadow:0 3px 12px rgba(0,0,0,.2)}
.a{position:absolute}
.brand{font-family:'Open Sans',sans-serif;font-weight:700;font-size:12px;color:var(--purple);letter-spacing:-.2px}
.brand.light{color:var(--white)}
.title{font-family:'Josefin Sans',sans-serif;font-weight:300;font-size:20px;line-height:1.1;letter-spacing:1px;color:var(--purple);text-transform:uppercase}
.title b{font-weight:700}
.title.white{color:var(--white)}
.body{font-size:5.2px;line-height:1.8;color:#444;text-align:justify}
.body.white{color:var(--white)}
.sub{font-size:6px;font-weight:700;color:var(--purple);text-transform:uppercase;letter-spacing:.3px}
.sub.white{color:var(--white)}
.foot{bottom:8px;font-size:4px;letter-spacing:1.6px;color:#9a9a9a}
.foot.white{color:rgba(255,255,255,.75)}
.photo-dark{background:linear-gradient(135deg,#2b2b30 0%,#4a4a52 55%,#b9a24a 100%)}
.photo-light{background:linear-gradient(135deg,#d9dde2 0%,#8f9aa6 60%,#3a3f46 100%)}
.photo-cards{background:linear-gradient(135deg,#eef1f4 0%,#b8c2cc 60%,#56606b 100%)}
.photo-desk{background:linear-gradient(135deg,#5d6168 0%,#2f3237 50%,#c9ccd2 100%)}
.marble{background:linear-gradient(120deg,#e8dccd 0%,#d4a77b 30%,#efe6da 50%,#c98a4f 70%,#f3ece4 100%)}
.fluid{background:radial-gradient(circle at 30% 30%,#c75fc1 0%,#7c2377 40%,#2a0d29 100%)}
.fluid-band{background:linear-gradient(90deg,#2a0d29 0%,#a33e9c 30%,#4a1446 55%,#b84faf 75%,#1c081b 100%)}
.icon-box{width:30px;height:28px;background:var(--purple);border-radius:3px;display:flex;align-items:center;justify-content:center}
.num-box{width:30px;height:30px;background:var(--purple);color:var(--white);font-family:'Josefin Sans',sans-serif;font-size:16px;display:flex;align-items:center;justify-content:center}
.circle{border-radius:50%;display:flex;align-items:center;justify-content:center}
.label{font-size:5.6px;color:var(--ink)}
.tiny{font-size:3.8px;line-height:1.6;color:#666}
</style>
</head>
<body>

<!-- Row 1 -->
<section class="slide" style="left:53px;top:36px">
  <div class="a marble" role="img" aria-label="Abstract marbled paint texture in cream and amber" style="left:0;top:0;width:480px;height:190px"></div>
  <div class="a" style="left:328px;top:30px;width:152px;height:240px;background:var(--orange)"></div>
  <div class="a brand light" style="left:342px;top:46px;font-size:20px">Pelminor</div>
  <div class="a" style="left:338px;top:79px;font-size:5.5px;letter-spacing:1.6px;color:var(--white);line-height:1.4">PELMINOR YOUR<br>TRUSTED PARTNER</div>
  <div class="a" style="left:66px;top:136px;width:328px;height:102px;background:var(--white);box-shadow:0 2px 6px rgba(0,0,0,.15)"></div>
  <div class="a title" style="left:100px;top:150px;font-size:21px;color:#555;text-align:center;width:260px">Place here your<br>title resentation</div>
  <div class="a" style="left:100px;top:214px;width:260px;text-align:center;font-size:7px;letter-spacing:1px;color:#555">Place here your subtitle presentation</div>
  <div class="a foot" style="left:158px">Confidential &amp; Propietart ©Pelminor 2022</div>
</section>

<section class="slide" style="left:451px;top:36px">
  <div class="a brand" style="left:30px;top:20px">Pelminor</div>
  <div class="a title" style="left:32px;top:112px">About <b>us</b></div>
  <div class="a body" style="left:32px;top:150px;width:175px">Pelminor provides state of the art, end-to-end payments processing solution to ensure we are your one-stop shop for your payment solution needs. Our payments domain expertise combined with implementation of proven technology solutions enables you to provide robust, secure, ease of use and cost-effective product and services to your customers.</div>
  <div class="a fluid" role="img" aria-label="Dark purple fluid ink texture" style="left:240px;top:42px;width:240px;height:188px"></div>
  <div class="a brand" style="left:272px;top:76px;font-size:24px;color:#e07fd9">Pelminor</div>
  <div class="a" style="left:290px;top:123px;width:16px;height:16px;background:var(--purple)"></div>
  <div class="a" style="left:312px;top:124px;font-size:8px;color:var(--white)">Credexa</div>
  <div class="a" style="left:312px;top:142px;font-size:8px;color:var(--white)">Payvora</div>
  <div class="a foot" style="left:32px">Confidential &amp; Propietart ©Pelminor 2022</div>
  <div class="a foot" style="left:345px">www.pelminor.com.sg &nbsp; 2</div>
</section>

<section class="slide" style="left:849px;top:36px">
  <div class="a title" style="left:43px;top:16px;font-size:17px">Table of <b>contents</b></div>
  <div class="a brand" style="left:384px;top:18px">Pelminor</div>
  <div class="a fluid-band" role="img" aria-label="Purple fluid texture band" style="left:0;top:64px;width:480px;height:58px"></div>
  <div class="a fluid-band" role="img" aria-label="Purple fluid texture band" style="left:0;top:128px;width:480px;height:57px"></div>
  <div class="a fluid-band" role="img" aria-label="Purple fluid texture band" style="left:0;top:191px;width:480px;height:56px"></div>
  <div class="a title white" style="left:34px;top:84px;font-weight:700">01</div>
  <div class="a sub white" style="left:82px;top:82px">About us</div>
  <div class="a tiny" style="left:82px;top:92px;color:#eee;width:130px">Pelminor at a glance, our story and mission</div>
  <div class="a title white" style="left:34px;top:147px;font-weight:700">02</div>
  <div class="a sub white" style="left:82px;top:145px">Projects</div>
  <div class="a tiny" style="left:82px;top:155px;color:#eee;width:130px">Current pipeline and customer rollouts</div>
  <div class="a title white" style="left:34px;top:210px;font-weight:700">03</div>
  <div class="a sub white" style="left:82px;top:208px">Our services</div>
  <div class="a tiny" style="left:82px;top:218px;color:#eee;width:130px">Issuing, acquiring and fraud prevention</div>
  <div class="a title white" style="left:256px;top:84px;font-weight:700">04</div>
  <div class="a sub white" style="left:302px;top:82px">Team</div>
  <div class="a tiny" style="left:302px;top:92px;color:#eee;width:140px">Leadership team and advisors</div>
  <div class="a title white" style="left:256px;top:147px;font-weight:700">05</div>
  <div class="a sub white" style="left:302px;top:145px">Portfolio</div>
  <div class="a tiny" style="left:302px;top:155px;color:#eee;width:140px">Use cases and case studies</div>
  <div class="a title white" style="left:256px;top:210px;font-weight:700">06</div>
  <div class="a sub white" style="left:302px;top:208px">Q&amp;A</div>
  <div class="a tiny" style="left:302px;top:218px;color:#eee;width:140px">Questions and next steps</div>
  <div class="a foot" style="left:32px">Confidential &amp; Propietart ©Pelminor 2022</div>
  <div class="a foot" style="left:345px">www.pelminor.com.sg &nbsp; 3</div>
</section>

<!-- Row 2 -->
<section class="slide" style="left:53px;top:228px">
  <div class="a brand" style="left:30px;top:20px">Pelminor</div>
  <div class="a title" style="left:30px;top:48px">Title lorem is<br><b>dummy text</b></div>
  <div class="a" style="left:30px;top:106px;width:36px;height:1.5px;background:var(--orange)"></div>
  <div class="a body" style="left:30px;top:118px;width:207px">Pelminor runs a complete payment platform on the cloud, offering API based card issuing, transaction acquiring, fraud prevention and e-commerce services. Our customer facing apps bring dynamic virtual cards, second factor checks and passwordless sign in to banks, merchants and fintechs across the region. We focus on business clients who need fast, secure and flexible payment tools that scale with their growth and their customers, and we support them from first launch to full rollout.</div>
  <div class="a photo-dark" role="img" aria-label="Photo of a hand tapping a phone on a card terminal" style="left:271px;top:12px;width:209px;height:116px"></div>
  <div class="a photo-light" role="img" aria-label="Photo of a hand holding a payment card beside a laptop" style="left:271px;top:133px;width:209px;height:115px"></div>
  <div class="a foot" style="left:30px">Confidential &amp; Propietart ©Pelminor 2022</div>
  <div class="a foot" style="left:345px">www.pelminor.com.sg &nbsp; 5</div>
</section>

<section class="slide" style="left:451px;top:228px">
  <div class="a brand" style="left:384px;top:20px">Pelminor</div>
  <div class="a title" style="left:0;top:44px;width:480px;text-align:center;font-size:17px">Solutions <b>&amp; services</b></div>
  <div class="a body" style="left:44px;top:68px;width:392px;text-align:center">Our digital payment services are uniquely positioned to address a vast Asia Pacific based clientele that fits with the key verticals, including: banks, financial services, telecom companies and national payment institutions.</div>
  <div class="a icon-box" style="left:46px;top:112px"><svg width="16" height="12" viewBox="0 0 16 12"><rect x="1" y="1" width="14" height="10" rx="1.5" fill="none" stroke="#fff" stroke-width="1.3"/><line x1="1" y1="5" x2="15" y2="5" stroke="#fff" stroke-width="1.3"/></svg></div>
  <div class="a label" style="left:94px;top:123px">Issuer Services</div>
  <div class="a icon-box" style="left:46px;top:154px"><svg width="16" height="14" viewBox="0 0 16 14"><path d="M2 5h12v8H2zM1 5l2-4h10l2 4" fill="none" stroke="#fff" stroke-width="1.3"/></svg></div>
  <div class="a label" style="left:94px;top:165px">Acquirer &amp; Merchant Services</div>
  <div class="a icon-box" style="left:46px;top:195px"><svg width="16" height="14" viewBox="0 0 16 14"><rect x="1" y="4" width="14" height="9" rx="1" fill="#fff"/><rect x="5" y="1" width="6" height="4" fill="none" stroke="#fff" stroke-width="1.3"/></svg></div>
  <div class="a label" style="left:94px;top:206px">Professional Services</div>
  <div class="a icon-box" style="left:262px;top:112px"><svg width="16" height="14" viewBox="0 0 16 14"><circle cx="8" cy="7" r="5.5" fill="none" stroke="#fff" stroke-width="1.3"/><path d="M6 4.5q2 2.5 0 5M9 3.5q3 3.5 0 7" fill="none" stroke="#fff" stroke-width="1.2"/></svg></div>
  <div class="a label" style="left:310px;top:123px">Contactless Payments</div>
  <div class="a icon-box" style="left:262px;top:154px"><svg width="16" height="14" viewBox="0 0 16 14"><path d="M1 2h2l2 8h8l2-6H4" fill="none" stroke="#fff" stroke-width="1.3"/><circle cx="6" cy="12.5" r="1" fill="#fff"/><circle cx="12" cy="12.5" r="1" fill="#fff"/></svg></div>
  <div class="a label" style="left:310px;top:165px">E-Commerce Services</div>
  <div class="a icon-box" style="left:262px;top:195px"><svg width="16" height="14" viewBox="0 0 16 14"><path d="M8 1v12M4 5v3l4 2M12 4v3l-4 2" fill="none" stroke="#fff" stroke-width="1.3"/></svg></div>
  <div class="a label" style="left:310px;top:202px;line-height:1.3">Advanced &amp; Future-Proof<br>Technologies</div>
  <div class="a foot" style="left:32px">Confidential &amp; Propietart ©Pelminor 2022</div>
  <div class="a foot" style="left:345px">www.pelminor.com.sg &nbsp; 4</div>
</section>

<section class="slide" style="left:849px;top:228px">
  <div class="a fluid" role="img" aria-label="Purple and pink fluid paint texture" style="left:0;top:0;width:156px;height:270px"></div>
  <div class="a title white" style="left:30px;top:46px;font-size:19px;line-height:1">Slide two<br>column&amp;<br><b>bullet</b><br><b>list</b></div>
  <div class="a brand" style="left:384px;top:20px">Pelminor</div>
  <div class="a sub" style="left:168px;top:52px">Subtitle slide lorem ipsum</div>
  <div class="a sub" style="left:328px;top:52px">Subtitle slide lorem ipsum</div>
  <div class="a" style="left:168px;top:68px;width:132px">
    <div class="tiny" style="text-align:justify;padding-left:9px;position:relative"><span class="a" style="left:0;top:1px;width:4px;height:4px;border:.7px solid var(--purple)"></span>Virtual cards are created on demand for every purchase, so stolen card numbers lose value and merchants see fewer disputes. Issuers can launch new card programmes in weeks through a single API, with controls for limits, merchants and validity set in real time by each customer.</div>
    <div class="tiny" style="text-align:justify;padding-left:9px;position:relative;margin-top:6px"><span class="a" style="left:0;top:1px;width:4px;height:4px;border:.7px solid var(--purple)"></span>Second factor checks run inside the app with a single tap, removing codes sent by text. Fewer steps at checkout mean fewer abandoned baskets and higher approval rates for every merchant we serve across the region today.</div>
  </div>
  <div class="a" style="left:328px;top:68px;width:132px">
    <div class="tiny" style="text-align:justify;padding-left:9px;position:relative"><span class="a" style="left:0;top:1px;width:4px;height:4px;border:.7px solid var(--purple)"></span>Passwordless sign in links a verified digital identity to each device, so users log in safely without passwords. Banks and fintechs cut support costs while account takeover fraud falls, and onboarding becomes quick and simple for every new customer joining the service.</div>
    <div class="tiny" style="text-align:justify;padding-left:9px;position:relative;margin-top:6px"><span class="a" style="left:0;top:1px;width:4px;height:4px;border:.7px solid var(--purple)"></span>The platform runs fully on the cloud, scales with demand and is ready for new markets such as airlines and insurance, with shared services that let partners add features without heavy new builds.</div>
  </div>
  <div class="a foot white" style="left:14px">Research Advancing Resilience</div>
  <div class="a foot" style="left:160px">bat 2022</div>
  <div class="a foot" style="left:345px">www.pelminor.com.sg &nbsp; 7</div>
</section>

<!-- Row 3 -->
<section class="slide" style="left:53px;top:420px">
  <div class="a title" style="left:37px;top:16px;font-size:17px">Four topic <b>&amp; bullet list</b></div>
  <div class="a brand" style="left:384px;top:20px">Pelminor</div>
  <div class="a" style="left:33px;top:64px;width:100px;height:176px;background:var(--card)"></div>
  <div class="a" style="left:136px;top:64px;width:100px;height:176px;background:var(--card)"></div>
  <div class="a" style="left:239px;top:64px;width:100px;height:176px;background:var(--card)"></div>
  <div class="a" style="left:342px;top:64px;width:100px;height:176px;background:var(--card)"></div>
  <div class="a num-box" style="left:42px;top:56px">1</div>
  <div class="a num-box" style="left:145px;top:56px">2</div>
  <div class="a num-box" style="left:248px;top:56px">3</div>
  <div class="a num-box" style="left:351px;top:56px">4</div>
  <div class="a sub" style="left:42px;top:96px;line-height:1.4">Subtitle slide a<br>lorem ipsum</div>
  <div class="a sub" style="left:145px;top:96px;line-height:1.4">Subtitle slide a<br>lorem ipsum</div>
  <div class="a sub" style="left:248px;top:96px;line-height:1.4">Subtitle slide a<br>lorem ipsum</div>
  <div class="a sub" style="left:351px;top:96px;line-height:1.4">Subtitle slide a<br>lorem ipsum</div>
  <div class="a tiny" style="left:42px;top:122px;width:86px;font-size:4.3px;color:#444;line-height:1.85">Banks launch card programmes fast through one simple API. Virtual cards cut fraud and chargebacks. Real-time controls set limits per customer. Reports show spend, trends and risk across every channel in one clear view for every team.<br><span style="color:var(--purple)">Faster card issuing.</span></div>
  <div class="a tiny" style="left:145px;top:122px;width:86px;font-size:4.3px;color:#444;line-height:1.85">Merchants accept cards online and in store with one link. Smart routing lifts approval rates. Fewer checkout steps mean fewer lost baskets. Settlement is quick and reports are clear for finance teams every single day.<br><span style="color:var(--purple)">Higher approval rates.</span></div>
  <div class="a tiny" style="left:248px;top:122px;width:86px;font-size:4.3px;color:#444;line-height:1.85">Fintechs add payments to their apps in days, not months. Ready modules cover cards, wallets and checks. Sandbox tools help teams test safely. Clear pricing grows with volume so start-ups can scale without surprise cost.<br><span style="color:var(--purple)">Launch in days.</span></div>
  <div class="a tiny" style="left:351px;top:122px;width:86px;font-size:4.3px;color:#444;line-height:1.85">Transport operators take tap to pay fares on every route. Digital ID speeds up rider sign in. Fraud tools flag odd use early. Open design lets new partners such as airlines and insurers join the platform later on.<br><span style="color:var(--purple)">Ready for new sectors.</span></div>
  <div class="a foot" style="left:32px">Confidential &amp; Propietart ©Pelminor 2022</div>
  <div class="a foot" style="left:345px">www.pelminor.com.sg &nbsp; 9</div>
</section>

<section class="slide" style="left:451px;top:420px">
  <div class="a title" style="left:33px;top:16px;font-size:18px;color:var(--orange)">Four topic &amp;<br><b>bullet list</b></div>
  <div class="a body" style="left:33px;top:78px;width:160px">The card payment market keeps growing as shoppers move online, yet many checkouts still fail. Card abandonment, weak sign in and rising fraud cost merchants and banks billions each year. Pelminor targets these gaps with virtual cards, in-app second factor checks and passwordless digital identity, all delivered from one cloud platform. Our services help issuers, acquirers and merchants approve more good payments, block more bad ones and give customers a smooth experience on every device they use.<br><br>Regional demand is strong and the global addressable market for payment cards is large and rising fast.</div>
  <div class="a" style="left:207px;top:0;width:273px;height:270px;background:var(--orange)"></div>
  <div class="a brand light" style="left:384px;top:20px">Pelminor</div>
  <div class="a circle" style="left:222px;top:54px;width:22px;height:28px;border-radius:2px;background:#fff;color:var(--orange);font-family:'Josefin Sans';font-size:13px">1</div>
  <div class="a circle" style="left:222px;top:100px;width:22px;height:28px;border-radius:2px;background:#fff;color:var(--orange);font-family:'Josefin Sans';font-size:13px">2</div>
  <div class="a circle" style="left:222px;top:147px;width:22px;height:28px;border-radius:2px;background:#fff;color:var(--orange);font-family:'Josefin Sans';font-size:13px">3</div>
  <div class="a circle" style="left:222px;top:193px;width:22px;height:28px;border-radius:2px;background:#fff;color:var(--orange);font-family:'Josefin Sans';font-size:13px">4</div>
  <div class="a" style="left:256px;top:48px;width:212px;color:#fff"><div style="font-size:5.4px">LOREM IPSUM DOLOR SIT AMET.</div><div class="tiny" style="color:#fff;font-size:4.2px">Card abandonment at checkout costs merchants a large share of online sales. One-tap checks keep buyers moving and raise completed orders.</div></div>
  <div class="a" style="left:256px;top:95px;width:212px;color:#fff"><div style="font-size:5.4px">LOREM IPSUM DOLOR SIT AMET.</div><div class="tiny" style="color:#fff;font-size:4.2px">Low approval rates turn away good customers. Smarter risk data and tokenised cards help issuers say yes with confidence.</div></div>
  <div class="a" style="left:256px;top:141px;width:212px;color:#fff"><div style="font-size:5.4px">LOREM IPSUM DOLOR SIT AMET.</div><div class="tiny" style="color:#fff;font-size:4.2px">Password resets and stolen logins drive cost and fraud. Passwordless digital ID removes the weak link for users and banks.</div></div>
  <div class="a" style="left:256px;top:187px;width:212px;color:#fff"><div style="font-size:5.4px;font-weight:700">LOREM IPSUM DOLOR SIT AMET.</div><div class="tiny" style="color:#fff;font-size:4.2px">Legacy systems slow new launches. Our cloud APIs let partners go live quickly and add features as markets change.</div></div>
  <div class="a foot" style="left:32px">Confidential &amp; Propietart ©Pelminor 2022</div>
  <div class="a foot white" style="left:370px">www.pelminor.com.sg &nbsp; 10</div>
</section>

<section class="slide" style="left:849px;top:420px">
  <div class="a title" style="left:34px;top:16px;font-size:17px">The problem <b>slide</b></div>
  <div class="a brand" style="left:384px;top:20px">Pelminor</div>
  <div class="a circle" style="left:59px;top:85px;width:54px;height:54px;background:#f3f3f3;font-family:'Josefin Sans';font-weight:700;font-size:11px">20%</div>
  <div class="a circle" style="left:153px;top:85px;width:54px;height:54px;background:var(--purple);color:#fff;font-family:'Josefin Sans';font-weight:700;font-size:11px">50%</div>
  <div class="a circle" style="left:247px;top:85px;width:54px;height:54px;background:#f3f3f3;font-family:'Josefin Sans';font-weight:700;font-size:11px">15%</div>
  <div class="a circle" style="left:341px;top:85px;width:54px;height:54px;background:#f3f3f3;font-family:'Josefin Sans';font-weight:700;font-size:11px">15%</div>
  <svg class="a" style="left:127px;top:107px" width="8" height="10" viewBox="0 0 8 10"><path d="M2 1l4 4-4 4" fill="none" stroke="var(--purple)" stroke-width="2"/></svg>
  <svg class="a" style="left:222px;top:107px" width="8" height="10" viewBox="0 0 8 10"><path d="M2 1l4 4-4 4" fill="none" stroke="var(--purple)" stroke-width="2"/></svg>
  <svg class="a" style="left:314px;top:107px" width="8" height="10" viewBox="0 0 8 10"><path d="M2 1l4 4-4 4" fill="none" stroke="var(--purple)" stroke-width="2"/></svg>
  <div class="a sub" style="left:60px;top:154px;color:#333">Sales problem</div>
  <div class="a sub" style="left:154px;top:154px;color:#333">Marketing problem</div>
  <div class="a sub" style="left:248px;top:154px;color:#333">Problem three</div>
  <div class="a sub" style="left:342px;top:154px;color:#333">Problem four</div>
  <div class="a tiny" style="left:60px;top:163px;width:72px">Lost card sales at checkout each year across the region</div>
  <div class="a tiny" style="left:154px;top:163px;width:72px">Share of online buyers who drop out at the payment step</div>
  <div class="a tiny" style="left:248px;top:163px;width:72px">Orders declined by issuers even though they are genuine</div>
  <div class="a tiny" style="left:342px;top:163px;width:72px">Logins lost to forgotten or stolen passwords each month</div>
  <div class="a foot" style="left:32px">Confidential &amp; Propietart ©Pelminor 2022</div>
  <div class="a foot" style="left:345px">www.pelminor.com.sg &nbsp; 12</div>
</section>

<!-- Row 4 -->
<section class="slide" style="left:53px;top:612px">
  <div class="a title" style="left:33px;top:16px;font-size:17px">Problem <b>&amp; solution</b></div>
  <div class="a brand" style="left:384px;top:20px">Pelminor</div>
  <svg class="a" style="left:0;top:0" width="480" height="270" viewBox="0 0 480 270">
    <g stroke="#c99cc5" stroke-width=".8" fill="none">
      <line x1="97" y1="150" x2="136" y2="150"/>
      <line x1="216" y1="150" x2="262" y2="150"/>
      <line x1="212" y1="132" x2="264" y2="92"/>
      <line x1="212" y1="168" x2="264" y2="206"/>
    </g>
  </svg>
  <div class="a circle" style="left:47px;top:125px;width:50px;height:50px;background:#f3f3f3;flex-direction:column">
    <svg width="12" height="11" viewBox="0 0 12 11"><rect x="1" y="3" width="10" height="7" fill="none" stroke="var(--purple)" stroke-width="1"/><rect x="4" y="1" width="4" height="2.5" fill="none" stroke="var(--purple)" stroke-width="1"/></svg>
    <span style="font-size:4.5px;font-weight:700;color:var(--purple)">PROBLEM</span>
  </div>
  <div class="a circle" style="left:136px;top:110px;width:80px;height:80px;background:var(--purple);flex-direction:column;color:#fff">
    <svg width="22" height="18" viewBox="0 0 22 18"><rect x="1" y="5" width="20" height="12" rx="1" fill="none" stroke="#fff" stroke-width="1.5"/><rect x="7" y="1" width="8" height="4" fill="none" stroke="#fff" stroke-width="1.5"/><line x1="1" y1="10" x2="21" y2="10" stroke="#fff" stroke-width="1.2"/></svg>
    <span style="font-size:6px;font-weight:700;margin-top:4px">SOLUTION</span>
  </div>
  <div class="a circle" style="left:262px;top:68px;width:48px;height:48px;background:#f3f3f3"><svg width="16" height="13" viewBox="0 0 16 13"><path d="M4 10a3 3 0 0 1 0-6 4 4 0 0 1 8 0 3 3 0 0 1 0 6z" fill="none" stroke="var(--purple)" stroke-width="1"/></svg></div>
  <div class="a circle" style="left:262px;top:126px;width:48px;height:48px;background:#f3f3f3"><svg width="14" height="14" viewBox="0 0 14 14"><path d="M2 6h3v7H2zM5 7l3-5q2 0 1 4h4l-1 7H5" fill="none" stroke="var(--purple)" stroke-width="1"/></svg></div>
  <div class="a circle" style="left:262px;top:184px;width:48px;height:48px;background:#f3f3f3"><svg width="16" height="14" viewBox="0 0 16 14"><path d="M4 1h8l3 4-7 8-7-8zM1 5h14M6 1l2 12 2-12" fill="none" stroke="var(--purple)" stroke-width="1"/></svg></div>
  <div class="a sub" style="left:323px;top:74px">Save energy</div>
  <div class="a tiny" style="left:323px;top:83px;width:64px">One cloud platform replaces many legacy systems.</div>
  <div class="a sub" style="left:323px;top:132px">Save money</div>
  <div class="a tiny" style="left:323px;top:141px;width:64px">Lower fraud and support costs for every partner.</div>
  <div class="a sub" style="left:323px;top:190px">Make money</div>
  <div class="a tiny" style="left:323px;top:199px;width:64px">More approved orders and fewer lost baskets.</div>
  <div class="a foot" style="left:32px">Confidential &amp; Propietart ©Pelminor 2022</div>
  <div class="a foot" style="left:345px">www.pelminor.com.sg &nbsp; 13</div>
</section>

<section class="slide" style="left:451px;top:612px">
  <div class="a title" style="left:33px;top:16px;font-size:17px">Solo text <b>slide</b></div>
  <div class="a brand" style="left:384px;top:20px">Pelminor</div>
  <svg class="a" style="left:0;top:0" width="480" height="270" viewBox="0 0 480 270">
    <line x1="0" y1="143" x2="480" y2="143" stroke="var(--purple)" stroke-width="4"/>
    <g stroke="#999" stroke-width=".6" fill="none">
      <path d="M58 121V64h10"/><path d="M148 121V64h6"/><path d="M196 121v-17h2"/><path d="M278 121v-17h2"/><path d="M362 121v-17h2"/><path d="M418 121V62h-10"/>
      <path d="M100 165v37h10"/><path d="M239 165v37h10"/><path d="M329 165v37h10"/>
    </g>
  </svg>
  <div class="a tiny" style="left:70px;top:60px">Founding</div>
  <div class="a tiny" style="left:156px;top:60px">Market Lorem</div>
  <div class="a tiny" style="left:366px;top:50px;width:48px;line-height:1.3">Market Lorem Ipsum is simply dummy</div>
  <div class="a tiny" style="left:198px;top:98px;line-height:1.3">2000+ Market<br>Lorem Ipsum is</div>
  <div class="a tiny" style="left:283px;top:98px;line-height:1.3">4000+ Market<br>Lorem Ipsum is</div>
  <div class="a tiny" style="left:368px;top:98px;line-height:1.3">6000+ Market<br>Lorem Ipsum is</div>
  <div class="a tiny" style="left:112px;top:197px;line-height:1.3">First Market<br>Lorem</div>
  <div class="a tiny" style="left:251px;top:197px;line-height:1.3">Market Lorem<br>Ipsum is simply<br>dummy text</div>
  <div class="a tiny" style="left:341px;top:200px;line-height:1.3">Lorem challenge<br>is simple</div>
  <div class="a circle" style="left:36px;top:121px;width:44px;height:44px;background:var(--purple);border:3px solid #e8d0e6;color:#fff;font-size:6px;text-align:center;line-height:1.2">2021<br>Q1</div>
  <div class="a circle" style="left:126px;top:121px;width:44px;height:44px;background:var(--purple);border:3px solid #e8d0e6;color:#fff;font-size:6px;text-align:center;line-height:1.2">2021<br>Q3</div>
  <div class="a circle" style="left:217px;top:121px;width:44px;height:44px;background:var(--purple);border:3px solid #e8d0e6;color:#fff;font-size:6px;text-align:center;line-height:1.2">2022<br>Q1</div>
  <div class="a circle" style="left:307px;top:121px;width:44px;height:44px;background:var(--purple);border:3px solid #e8d0e6;color:#fff;font-size:6px;text-align:center;line-height:1.2">2022<br>Q2</div>
  <div class="a circle" style="left:398px;top:121px;width:44px;height:44px;background:var(--purple);border:3px solid #e8d0e6;color:#fff;font-size:6px;text-align:center;line-height:1.2">2022<br>Q4</div>
  <div class="a foot" style="left:32px">Confidential &amp; Propietart ©Pelminor 2022</div>
  <div class="a foot" style="left:345px">www.pelminor.com.sg &nbsp; 14</div>
</section>

<section class="slide" style="left:849px;top:612px">
  <div class="a brand" style="left:30px;top:20px">Pelminor</div>
  <div class="a title" style="left:30px;top:66px;font-size:17px">Title lorem<br>ipsum is<br><b>dummy text</b></div>
  <div class="a" style="left:30px;top:140px;font-size:6px;color:var(--purple)">LOREM IPSUM DOLOR &nbsp;AMET</div>
  <div class="a body" style="left:30px;top:152px;width:122px;font-size:4.6px">Pelminor helps banks, merchants and fintechs accept, issue and protect card payments with one cloud platform. Virtual cards, in-app checks and digital identity work together to lift approvals and cut fraud for every client segment we serve.</div>
  <div class="a photo-dark" role="img" aria-label="Photo of a phone payment at a card terminal" style="left:176px;top:14px;width:128px;height:72px"></div>
  <div class="a photo-light" role="img" aria-label="Photo of a card held beside a laptop" style="left:176px;top:96px;width:128px;height:72px"></div>
  <div class="a photo-cards" role="img" aria-label="Photo of a hand holding several payment cards" style="left:176px;top:178px;width:128px;height:72px"></div>
  <div class="a" style="left:326px;top:28px;width:130px"><div style="font-size:5.4px;font-weight:700;color:var(--purple)">LOREM IPSUM DOLOR AMET</div><div class="tiny" style="color:#444;text-align:justify">Issuers launch virtual card programmes in weeks with full real-time controls.</div></div>
  <div class="a" style="left:326px;top:110px;width:130px"><div style="font-size:5.4px;font-weight:700;color:var(--purple)">LOREM IPSUM DOLOR AMET</div><div class="tiny" style="color:#444;text-align:justify">Merchants reduce checkout drop out with one-tap second factor checks.</div></div>
  <div class="a" style="left:326px;top:192px;width:130px"><div style="font-size:5.4px;font-weight:700;color:var(--purple)">LOREM IPSUM DOLOR AMET</div><div class="tiny" style="color:#444;text-align:justify">Users sign in without passwords through a verified digital identity.</div></div>
  <div class="a foot" style="left:32px">Confidential &amp; Propietart ©Pelminor 2022</div>
  <div class="a foot" style="left:345px">www.pelminor.com.sg &nbsp; 15</div>
</section>

<!-- Row 5 -->
<section class="slide" style="left:53px;top:805px">
  <div class="a brand" style="left:30px;top:20px">Pelminor</div>
  <div class="a title" style="left:28px;top:52px;font-size:17px">Title lorem<br>ipsum is<br><b>dummy text</b></div>
  <div class="a" style="left:190px;top:56px;font-size:5.8px;font-weight:700;color:var(--purple)">LOREM IPSUM IS SIMPLY DUMMY TEXT PRINTING</div>
  <div class="a body" style="left:190px;top:66px;width:252px;font-size:4.8px">Pelminor brings card issuing, acquiring, fraud prevention and e-commerce services together on one cloud platform. Partners connect once through our APIs and gain virtual cards, in-app second factor checks and passwordless sign in, helping them raise approval rates and cut fraud costs.</div>
  <div class="a" style="left:0;top:134px;width:480px;height:136px;background:var(--purple)"></div>
  <svg class="a" style="left:30px;top:146px" width="22" height="22" viewBox="0 0 22 22"><circle cx="11" cy="11" r="9" fill="none" stroke="#fff" stroke-width="1.4"/><circle cx="11" cy="11" r="5" fill="none" stroke="#fff" stroke-width="1.4"/><circle cx="11" cy="11" r="1.6" fill="#fff"/></svg>
  <svg class="a" style="left:180px;top:146px" width="22" height="22" viewBox="0 0 22 22"><circle cx="11" cy="11" r="7" fill="none" stroke="#fff" stroke-width="1.4"/><path d="M11 1v20M1 11h20" stroke="#fff" stroke-width="1.2"/></svg>
  <svg class="a" style="left:325px;top:146px" width="22" height="22" viewBox="0 0 22 22"><circle cx="9" cy="9" r="7" fill="none" stroke="#fff" stroke-width="1.4"/><path d="M14 14l6 6M5 10l2-2 2 2 3-4" fill="none" stroke="#fff" stroke-width="1.4"/></svg>
  <div class="a sub white" style="left:30px;top:180px">Lorem ipsum dolor amet</div>
  <div class="a sub white" style="left:180px;top:180px">Lorem ipsum dolor amet</div>
  <div class="a sub white" style="left:325px;top:180px">Lorem ipsum dolor amet</div>
  <div class="a tiny" style="left:30px;top:192px;width:125px;color:#fff;text-align:justify">Card issuing through one API with full controls and clear reporting for issuers.</div>
  <div class="a tiny" style="left:180px;top:192px;width:125px;color:#fff;text-align:justify">Smart acquiring that lifts approval rates for merchants online and in store.</div>
  <div class="a tiny" style="left:325px;top:192px;width:125px;color:#fff;text-align:justify">Fraud prevention that spots risk early and protects every customer account.</div>
  <div class="a foot white" style="left:32px">Research Advancing Resilience</div>
  <div class="a foot white" style="left:345px">www.pelminor.com.sg &nbsp; 16</div>
</section>

<section class="slide" style="left:451px;top:805px">
  <div class="a fluid" role="img" aria-label="Purple fluid ink texture" style="left:275px;top:0;width:205px;height:270px"></div>
  <div class="a brand light" style="left:384px;top:20px">Pelminor</div>
  <div class="a title" style="left:38px;top:30px;font-size:16px">Title lorem ipsum<br><b>is dummy text</b></div>
  <div class="a" style="left:38px;top:88px;font-size:5.6px;font-weight:700;color:var(--purple)">LOREM IPSUM DOLOR IS AMET CONS</div>
  <div class="a body" style="left:38px;top:98px;width:222px;font-size:4.8px">Our cloud platform gives partners virtual cards, second factor checks and passwordless sign in through one set of APIs. Banks, merchants and fintechs launch faster, approve more good orders and block more fraud across every channel.</div>
  <div class="a" style="left:32px;top:155px;width:130px;height:87px;background:var(--purple);padding:10px"><div style="font-size:5.4px;font-weight:700;color:#fff">LOREM IPSUM DOLOR</div><div class="tiny" style="color:#fff;margin-top:4px;text-align:justify">Virtual cards made for each purchase keep card details safe and cut disputes.</div></div>
  <div class="a" style="left:172px;top:155px;width:130px;height:87px;background:var(--purple);padding:10px"><div style="font-size:5.4px;font-weight:700;color:#fff">LOREM IPSUM DOLOR</div><div class="tiny" style="color:#fff;margin-top:4px;text-align:justify">One-tap checks in the app replace text codes and keep buyers at checkout.</div></div>
  <div class="a" style="left:312px;top:155px;width:130px;height:87px;background:#fff;padding:10px"><div style="font-size:5.4px;font-weight:700;color:#333">LOREM IPSUM DOLOR</div><div class="tiny" style="color:#444;margin-top:4px;text-align:justify">Digital identity lets users sign in with no password on any device.</div></div>
  <div class="a foot" style="left:32px">Confidential &amp; Propietart ©Pelminor 2022</div>
  <div class="a foot white" style="left:345px">www.pelminor.com.sg &nbsp; 17</div>
</section>

<section class="slide" style="left:849px;top:805px">
  <div class="a" role="img" aria-label="Photo of a phone tapped on a card terminal" style="left:290px;top:0;width:190px;height:270px;background:linear-gradient(135deg,#c9d6e2 0%,#5d6b7a 45%,#1e2228 75%,#c3b13d 100%)"></div>
  <div class="a brand" style="left:30px;top:20px">Pelminor</div>
  <div class="a title" style="left:30px;top:56px;font-size:17px">Title lorem is<br><b>dummy text</b></div>
  <div class="a" style="left:30px;top:116px;font-size:5.6px;font-weight:700;color:var(--purple)">LOREM IPSUM DOLOR IS AMET</div>
  <div class="a body" style="left:30px;top:128px;width:188px;font-size:4.8px">Pelminor helps partners approve more genuine card payments while stopping fraud early. Our virtual cards, in-app second factor checks and passwordless digital identity work from one cloud platform and connect through simple APIs. Issuers, merchants and fintechs see quicker launches, higher approval rates, fewer abandoned baskets and lower support costs, with clear data to track results over time.</div>
  <div class="a" style="left:238px;top:30px;width:66px;height:66px;background:var(--purple);color:#fff;text-align:center;padding-top:6px">
    <svg width="14" height="14" viewBox="0 0 14 14"><circle cx="7" cy="7" r="6" fill="none" stroke="#fff" stroke-width="1.1"/><circle cx="7" cy="7" r="2.5" fill="none" stroke="#fff" stroke-width="1.1"/></svg>
    <div style="font-size:8px;margin-top:4px">80%</div><div style="font-size:4px;margin-top:3px">Text Title First</div></div>
  <div class="a" style="left:238px;top:104px;width:66px;height:66px;background:var(--purple);color:#fff;text-align:center;padding-top:6px">
    <svg width="16" height="12" viewBox="0 0 16 12"><path d="M1 6q7-9 14 0-7 9-14 0z" fill="none" stroke="#fff" stroke-width="1.1"/><circle cx="8" cy="6" r="2" fill="#fff"/></svg>
    <div style="font-size:8px;margin-top:4px">70%</div><div style="font-size:4px;margin-top:3px">Text Tittle Second</div></div>
  <div class="a" style="left:238px;top:178px;width:66px;height:66px;background:var(--purple);color:#fff;text-align:center;padding-top:6px">
    <svg width="14" height="12" viewBox="0 0 14 12"><path d="M3 1h8l2 3-6 7-6-7zM1 4h12" fill="none" stroke="#fff" stroke-width="1.1"/></svg>
    <div style="font-size:8px;margin-top:4px">95%</div><div style="font-size:4px;margin-top:3px">Text Tittle Third</div></div>
  <div class="a foot" style="left:32px">Confidential &amp; Propietart ©Pelminor 2022</div>
  <div class="a foot white" style="left:345px">www.pelminor.com.sg &nbsp; 18</div>
</section>

<!-- Row 6 -->
<section class="slide" style="left:53px;top:997px">
  <div class="a brand" style="left:30px;top:20px">Pelminor</div>
  <div class="a title" style="left:30px;top:56px;font-size:17px">Title lorem is<br><b>dummy text</b></div>
  <div class="a" style="left:30px;top:118px;font-size:5.6px;font-weight:700;color:var(--purple)">LOREM IPSUM DOLOR IS AMET</div>
  <div class="a body" style="left:30px;top:130px;width:182px;font-size:4.8px">Pelminor products cover the full card journey. Issuing tools create physical and virtual cards, acquiring services process payments online and in store, fraud tools score every transaction and our apps give users dynamic cards, one-tap checks and passwordless sign in. Each product connects through the same cloud APIs, so partners can start small and add more services as they grow into new markets and segments.</div>
  <div class="a photo-desk" role="img" aria-label="Photo of a tablet and phone used for payments on a desk" style="left:239px;top:32px;width:99px;height:98px"></div>
  <div class="a photo-dark" role="img" aria-label="Photo of a phone near a card terminal" style="left:342px;top:32px;width:99px;height:98px"></div>
  <div class="a photo-light" role="img" aria-label="Photo of a card held beside a laptop" style="left:239px;top:136px;width:99px;height:99px"></div>
  <div class="a photo-cards" role="img" aria-label="Photo of a hand holding payment cards" style="left:342px;top:136px;width:99px;height:99px"></div>
  <div class="a" style="left:239px;top:116px;width:99px;height:14px;background:var(--purple);color:#fff;font-size:5px;display:flex;align-items:center;justify-content:center">Product First</div>
  <div class="a" style="left:342px;top:116px;width:99px;height:14px;background:var(--purple);color:#fff;font-size:5px;display:flex;align-items:center;justify-content:center">Product Second</div>
  <div class="a" style="left:239px;top:221px;width:99px;height:14px;background:var(--purple);color:#fff;font-size:5px;display:flex;align-items:center;justify-content:center">Product Third</div>
  <div class="a" style="left:342px;top:221px;width:99px;height:14px;background:var(--purple);color:#fff;font-size:5px;display:flex;align-items:center;justify-content:center">Product Fourth</div>
  <div class="a foot" style="left:32px">Confidential &amp; Propietart ©Pelminor 2022</div>
  <div class="a foot" style="left:345px">www.pelminor.com.sg &nbsp; 19</div>
</section>

<section class="slide" style="left:451px;top:997px">
  <div class="a" style="left:0;top:0;width:197px;height:270px;background:var(--purple)"></div>
  <div class="a brand" style="left:384px;top:20px">Pelminor</div>
  <div class="a photo-light" role="img" aria-label="Photo of a card held beside a laptop" style="left:26px;top:54px;width:146px;height:113px"></div>
  <div class="a photo-desk" role="img" aria-label="Photo of a tablet and phone on a desk" style="left:179px;top:54px;width:146px;height:113px"></div>
  <div class="a photo-dark" role="img" aria-label="Photo of a phone near a card terminal" style="left:333px;top:54px;width:147px;height:113px"></div>
  <div class="a title white" style="left:30px;top:188px;font-size:16px">Lorem ipsum<br><b>dummy text</b></div>
  <div class="a" style="left:30px;top:231px;font-size:5.4px;letter-spacing:1.6px;color:#fff;font-weight:700">LOREM IPSUM DOLOR AMET</div>
  <div class="a body" style="left:225px;top:184px;width:218px;font-size:4.8px">Our use cases span banks launching virtual card programmes, merchants lifting approval rates at checkout, fintechs adding payments to their apps and transport operators taking tap to pay fares. Each project shows faster launch times, fewer abandoned orders and lower fraud losses for our partners in the region.</div>
  <div class="a foot" style="left:345px">www.pelminor.com.sg &nbsp; 20</div>
</section>

<section class="slide" style="left:849px;top:997px">
  <div class="a fluid" role="img" aria-label="Purple and pink fluid ink texture" style="left:18px;top:0;width:194px;height:238px"></div>
  <div class="a title white" style="left:45px;top:142px;font-size:26px">Thanks</div>
  <div class="a" style="left:45px;top:172px;width:150px;height:.8px;background:rgba(255,255,255,.6)"></div>
  <div class="a title white" style="left:45px;top:180px;font-size:15px">Contact us</div>
  <div class="a brand" style="left:384px;top:20px">Pelminor</div>
  <div class="a circle" style="left:258px;top:36px;width:24px;height:24px;background:var(--purple)"><svg width="11" height="8" viewBox="0 0 11 8"><rect x=".5" y=".5" width="10" height="7" fill="#fff"/><path d="M.5 .5l5 4 5-4" fill="none" stroke="var(--purple)" stroke-width=".9"/></svg></div>
  <div class="a circle" style="left:258px;top:86px;width:24px;height:24px;background:var(--purple)"><svg width="10" height="10" viewBox="0 0 10 10"><path d="M2 1l2 2-1 1.5q1 2 2.5 2.5L7 6l2 2-1.5 1.5Q1 8 .5 2.5z" fill="#fff"/></svg></div>
  <div class="a circle" style="left:258px;top:136px;width:24px;height:24px;background:var(--purple)"><svg width="11" height="10" viewBox="0 0 11 10"><rect x=".5" y=".5" width="10" height="7" fill="none" stroke="#fff" stroke-width="1"/><path d="M4 9.5h3" stroke="#fff" stroke-width="1"/></svg></div>
  <div class="a circle" style="left:258px;top:186px;width:24px;height:24px;background:var(--purple)"><svg width="8" height="11" viewBox="0 0 8 11"><rect x=".5" y=".5" width="7" height="10" fill="#fff"/><path d="M2 3h1M5 3h1M2 5.5h1M5 5.5h1" stroke="var(--purple)" stroke-width="1"/></svg></div>
  <div class="a" style="left:294px;top:36px;width:130px;border-bottom:.6px solid #ddd;padding-bottom:2px"><div style="font-size:5px;font-weight:700;color:var(--purple)">EMAIL</div><div style="font-size:6px">info@pelminor.com</div></div>
  <div class="a" style="left:294px;top:86px;width:130px;border-bottom:.6px solid #ddd;padding-bottom:2px"><div style="font-size:5px;font-weight:700;color:var(--purple)">PHONE</div><div style="font-size:6px">001-555- 2468-1357</div></div>
  <div class="a" style="left:294px;top:136px;width:130px;border-bottom:.6px solid #ddd;padding-bottom:2px"><div style="font-size:5px;font-weight:700;color:var(--purple)">WEBSITE</div><div style="font-size:6px">www. pelminor.com</div></div>
  <div class="a" style="left:294px;top:186px;width:130px"><div style="font-size:5px;font-weight:700;color:var(--purple)">OFFICE</div><div style="font-size:6px;line-height:1.3">Lorem Ipsum is simply dummy<br>text of the printing industry</div></div>
  <div class="a foot" style="left:32px">Confidential &amp; Propietart ©Pelminor 2022</div>
  <div class="a foot" style="left:345px">www.pelminor.com.sg &nbsp; 21</div>
</section>

</body>
</html>
```